Operating Model for KTR

Please convert the diagram on slide 3 to a professional design. Slides 1 and 2 gives a sense of the colour scheme - although not as bold as those - but sympathetic colours. But the KTR logo is to appear on the slide.
Further instructions in the slide

```html
<!DOCTYPE html>
<html lang="en">
<head>
<meta charset="utf-8">
<title>Operating Model for KTR</title>
<link rel="stylesheet" href="https://fonts.googleapis.com/css2?family=Arimo:wght@400;700&display=swap">
<style>
:root{
  --page:#d5d5d7;
  --stage-top:#e9ebee;
  --stage-bottom:#d9d6d0;
  --ink:#111111;
  --text:#3a3a3a;
  --muted:#6a6a6a;
  --white:#ffffff;
  --black:#000000;
  --red:#c8102e;
  --deep-red:#a81c22;
  --berry:#a4105a;
  --plum:#7a0c2e;
  --coral:#e8704a;
  --orange:#f08a4b;
}
*{box-sizing:border-box;margin:0;padding:0}
html,body{width:1200px;height:3356px;overflow:hidden}
body{background:var(--page);font-family:"Arimo",Arial,sans-serif;color:var(--ink);position:relative}

.stage{position:absolute;left:0;top:0;width:1200px;height:712px;background:linear-gradient(180deg,var(--stage-top),var(--stage-bottom))}
.stage-frame{position:absolute;left:319px;top:198px;width:562px;height:316px;overflow:hidden;box-shadow:0 10px 30px rgba(0,0,0,.18)}
.stage-frame .slide{transform:scale(.5);transform-origin:0 0;left:0;top:0}

.slide{position:absolute;left:38px;width:1124px;height:632px;overflow:hidden;background:var(--white)}
.slide--title{top:726px}
.slide--content{top:1377px}
.slide--model{top:2029px}
.slide--contact{top:2680px}

.pattern{position:absolute;inset:0;background:linear-gradient(125deg,#b8212a 0%,#c1344e 35%,#a81c22 60%,#d0452f 85%,#a81c22 100%)}
.lens{position:absolute;inset:0}

.brand{position:absolute;display:flex;align-items:center;gap:12px;color:var(--white);font-weight:700}
.brand-dot{width:34px;height:34px;border-radius:50%;background:var(--red)}
.brand-name{font-size:30px;letter-spacing:.5px}
.slide--title .brand,.slide--contact .brand{left:129px}
.slide--title .brand{top:82px}
.slide--contact .brand{top:232px}

.title{position:absolute;left:129px;top:215px;font-size:52px;line-height:56px;font-weight:700;color:var(--white)}
.accent-bar{position:absolute;height:5px;border-radius:3px;background:linear-gradient(90deg,var(--red),var(--orange))}
.slide--title .accent-bar{left:129px;top:341px;width:185px}
.subtitle{position:absolute;left:129px;top:370px;font-size:22px;color:var(--white)}
.date{position:absolute;left:129px;top:423px;font-size:13px;letter-spacing:.6px;color:var(--white)}
.org{position:absolute;left:129px;top:512px;display:flex;align-items:center;gap:12px;color:var(--white)}
.org-name{font-size:18px;font-weight:700}
.org-rule{width:1px;height:30px;background:var(--white)}
.org-unit{font-size:11px;line-height:12px}

.heading{position:absolute;left:53px;top:45px;font-size:36px;font-weight:400;color:var(--ink)}
.heading strong{font-weight:700}
.slide--content .accent-bar{left:53px;top:104px;width:185px;height:4px}
.body-copy{position:absolute;left:53px;top:163px;width:565px;font-size:15px;line-height:17.5px;color:var(--text)}
.body-copy p{margin-bottom:12px}
.photo{position:absolute;left:663px;top:0;width:407px;height:545px;background:linear-gradient(160deg,#5c6670 0%,#8a8f94 35%,#e6823a 60%,#b9bcbf 85%,#4a4f55 100%)}

.footer-brand{position:absolute;left:30px;top:578px;display:flex;align-items:center;gap:8px;font-size:16px;font-weight:700;color:var(--ink)}
.footer-brand .brand-dot{width:20px;height:20px}
.copyright{position:absolute;right:68px;top:586px;font-size:10px;color:var(--muted)}
.page-no{position:absolute;right:30px;top:580px;width:22px;height:22px;border-radius:50%;background:var(--red);color:var(--white);font-size:10px;display:flex;align-items:center;justify-content:center}

.model{position:absolute;inset:0;font-family:"Arimo",Arial,sans-serif}
.label{font-size:15px;fill:var(--ink)}
.label-b{font-weight:700}
.ring-text{font-size:12px;letter-spacing:1.6px;fill:var(--ink)}
.inner-text{font-size:8px;font-weight:700;letter-spacing:.4px;fill:var(--ink)}
.node-text{font-size:7px;font-weight:700;fill:var(--white)}
.core-text{font-size:11px;font-weight:700}
.core-text--plan{fill:var(--red)}
.core-text--renew{fill:var(--coral)}

.contact-heading{position:absolute;left:129px;top:330px;font-size:22px;font-weight:700;color:var(--white)}
.contact-list{position:absolute;left:129px;top:382px;list-style:none;color:var(--white);font-size:16px}
.contact-list li{display:flex;align-items:center;gap:14px;height:32px}
.contact-list svg{width:22px;height:22px}
</style>
</head>
<body>

<section class="stage">
  <div class="stage-frame">
    <div class="slide">
      <div class="pattern" role="img" aria-label="Woven red, berry and coral ribbon pattern"></div>
      <svg class="lens" viewBox="0 0 1124 632"><path d="M118,0 L470,0 Q690,140 780,316 Q690,490 470,632 L110,632 Q30,480 40,316 Q40,130 118,0 Z" fill="#000"/></svg>
      <div class="brand"><span class="brand-dot"></span><span class="brand-name">KTR</span></div>
      <h1 class="title">Presentation Title<br>Goes Here</h1>
      <div class="accent-bar"></div>
      <p class="subtitle">Subtitle Of Presentation Goes Here</p>
      <p class="date">Friday, January 20, 2023</p>
      <div class="org"><span class="org-name">NORTHGATE</span><span class="org-rule"></span><span class="org-unit">Education<br>and Training</span></div>
    </div>
  </div>
</section>

<section class="slide slide--title">
  <div class="pattern" role="img" aria-label="Woven red, berry and coral ribbon pattern"></div>
  <svg class="lens" viewBox="0 0 1124 632"><path d="M118,0 L470,0 Q690,140 780,316 Q690,490 470,632 L110,632 Q30,480 40,316 Q40,130 118,0 Z" fill="#000"/></svg>
  <div class="brand"><span class="brand-dot"></span><span class="brand-name">KTR</span></div>
  <h1 class="title">Presentation Title<br>Goes Here</h1>
  <div class="accent-bar"></div>
  <p class="subtitle">Subtitle Of Presentation Goes Here</p>
  <p class="date">Friday, January 20, 2023</p>
  <div class="org"><span class="org-name">NORTHGATE</span><span class="org-rule"></span><span class="org-unit">Education<br>and Training</span></div>
</section>

<section class="slide slide--content">
  <h2 class="heading"><strong>Heading</strong> Goes Here</h2>
  <div class="accent-bar"></div>
  <div class="body-copy">
    <p>Lorem ipsum dolor sit amet, consectetur adipiscing elit. Vivamus eu dui ex. Curabitur dapibus dignissim dui, in molestie metus feugiat sed. Praesent aliquet lorem ex, eu dapibus odio varius at. Duis eget tellus porta, consequat lacus vitae, venenatis dolor. Nulla facilisi. In et sollicitudin lacus.</p>
    <p>Donec risus orci, gravida sit amet risus vehicula, aliquet pretium sapien. Nullam sit amet magna non ex bibendum mollis. Nunc vel neque eu augue dignissim congue ut vitae magna. Phasellus eget commodo arcu. Nunc vitae semper dui. Integer venenatis, tellus sit amet interdum pretium, erat neque rhoncus turpis, a aliquam augue ligula eget erat.</p>
    <p>Nunc placerat, arcu nec mattis fermentum, nisi mauris convallis nunc, ut luctus nunc nisl id ex. Nam semper tristique mauris, et vestibulum leo fringilla vel. Nulla id augue eleifend, egestas ligula et, consequat massa. Pellentesque habitant morbi tristique senectus et netus et malesuada fames ac turpis egestas.</p>
    <p>Lorem ipsum dolor sit amet, consectetur adipiscing elit. Vivamus eu dui ex. Curabitur dapibus dignissim dui, in molestie metus feugiat sed. Praesent aliquet lorem ex, eu dapibus odio varius at.</p>
  </div>
  <div class="photo" role="img" aria-label="Photo of a trainee in orange high-visibility workwear operating a forklift"></div>
  <div class="footer-brand"><span class="brand-dot"></span>KTR</div>
  <p class="copyright">Copyright © 2023  KTR</p>
  <div class="page-no">2</div>
</section>

<section class="slide slide--model">
  <svg class="model" viewBox="0 0 1124 632">
    <defs>
      <path id="arc-top" d="M357.2,187.6 A250,250 0 0 1 583.8,82"/>
      <path id="arc-left" d="M381,512 A256,256 0 0 1 314.7,264.7"/>
      <path id="arc-right" d="M771.7,184.2 A256,256 0 0 1 771.7,477.8"/>
      <path id="arc-inner-top" d="M513.8,262.2 A84,84 0 0 1 621.4,271.6"/>
      <path id="arc-inner-left" d="M493.2,379.2 A84,84 0 0 1 497.7,277"/>
      <path id="arc-inner-right" d="M640.9,302.3 A84,84 0 0 1 621.4,390.4"/>
      <path id="arc-inner-bottom" d="M554.7,414.7 A84,84 0 0 1 502.6,390.4"/>
    </defs>

    <text class="label" x="562" y="51" text-anchor="middle"><tspan class="label-b">Student</tspan> Acquisition and Guidance</text>

    <g class="segments" stroke="#fff" stroke-width="4" stroke-linejoin="round">
      <path d="M470.9,111.1 A238,238 0 0 1 653.1,111.1 L604.1,229.4 A110,110 0 0 0 519.9,229.4 Z" fill="var(--red)"/>
      <path d="M653.1,111.1 A238,238 0 0 1 781.9,239.9 L663.6,288.9 A110,110 0 0 0 604.1,229.4 Z" fill="var(--berry)"/>
      <path d="M781.9,239.9 A238,238 0 0 1 781.9,422.1 L663.6,373.1 A110,110 0 0 0 663.6,288.9 Z" fill="var(--coral)"/>
      <path d="M781.9,422.1 A238,238 0 0 1 653.1,550.9 L604.1,432.6 A110,110 0 0 0 663.6,373.1 Z" fill="var(--red)"/>
      <path d="M470.9,550.9 A238,238 0 0 1 342.1,422.1 L460.4,373.1 A110,110 0 0 0 519.9,432.6 Z" fill="var(--red)"/>
      <path d="M342.1,422.1 A238,238 0 0 1 342.1,239.9 L460.4,288.9 A110,110 0 0 0 460.4,373.1 Z" fill="var(--berry)"/>
      <path d="M342.1,239.9 A238,238 0 0 1 470.9,111.1 L519.9,229.4 A110,110 0 0 0 460.4,288.9 Z" fill="var(--coral)"/>
    </g>

    <circle cx="562" cy="331" r="106" fill="var(--plum)"/>
    <circle cx="562" cy="331" r="94" fill="#fff"/>

    <g class="icons" fill="#fff">
      <g transform="translate(562 157)"><circle cy="-7" r="7"/><path d="M-12,14 q12,-18 24,0 z"/></g>
      <g transform="translate(685 208)"><rect x="-11" y="-16" width="22" height="13" rx="2"/><circle cy="5" r="5"/><path d="M-9,17 q9,-12 18,0 z"/></g>
      <g transform="translate(736 331)"><rect x="-12" y="2" width="5" height="10"/><rect x="-4" y="-4" width="5" height="16"/><rect x="4" y="-10" width="5" height="22"/><path d="M-12,-6 l10,-6 l8,2 l6,-4" fill="none" stroke="#fff" stroke-width="2"/></g>
      <g transform="translate(685 454)"><circle r="11" fill="none" stroke="#fff" stroke-width="5" stroke-dasharray="4 3"/><circle r="4"/></g>
      <g transform="translate(439 454)"><circle cx="-6" cy="-6" r="6"/><circle cx="7" cy="-6" r="6"/><path d="M-16,12 q10,-16 20,0 z M-3,12 q10,-16 20,0 z"/></g>
      <g transform="translate(388 331)"><rect x="-13" y="-10" width="26" height="17" rx="2" fill="none" stroke="#fff" stroke-width="3"/><rect x="-17" y="9" width="34" height="3"/></g>
      <g transform="translate(439 208)"><circle cy="-4" r="9" fill="none" stroke="#fff" stroke-width="3"/><rect x="-4" y="7" width="8" height="7"/></g>
    </g>

    <text class="ring-text"><textPath href="#arc-top" startOffset="8%">ATTRACTING STUDENTS</textPath></text>
    <text class="ring-text"><textPath href="#arc-left" startOffset="12%">PLANNING FOR SKILLING</textPath></text>
    <text class="ring-text"><textPath href="#arc-right" startOffset="16%">BUILDING FUTURE SKILLS</textPath></text>

    <text class="inner-text"><textPath href="#arc-inner-top" startOffset="50%" text-anchor="middle">VOCATIONAL EDUCATION</textPath></text>
    <text class="inner-text"><textPath href="#arc-inner-left" startOffset="50%" text-anchor="middle">COMMUNITY EDUCATION</textPath></text>
    <text class="inner-text"><textPath href="#arc-inner-right" startOffset="50%" text-anchor="middle">HIGHER EDUCATION</textPath></text>
    <text class="inner-text"><textPath href="#arc-inner-bottom" startOffset="50%" text-anchor="middle">SCHOOLS</textPath></text>

    <g class="nodes" text-anchor="middle">
      <circle cx="562" cy="273" r="16" fill="var(--red)"/><text class="node-text" x="562" y="271">Comm<tspan x="562" dy="8">unity</tspan></text>
      <circle cx="603" cy="290" r="16" fill="var(--red)"/><text class="node-text" x="603" y="288">Indus<tspan x="603" dy="8">try</tspan></text>
      <circle cx="620" cy="331" r="16" fill="var(--red)"/><text class="node-text" x="620" y="329">Studen<tspan x="620" dy="8">ts</tspan></text>
      <circle cx="603" cy="372" r="16" fill="var(--coral)"/><text class="node-text" x="603" y="370">Feedb<tspan x="603" dy="8">ack</tspan></text>
      <circle cx="562" cy="389" r="16" fill="var(--coral)"/><text class="node-text" x="562" y="391.5">Quality</text>
      <circle cx="521" cy="372" r="16" fill="var(--coral)"/><text class="node-text" x="521" y="370">Produc<tspan x="521" dy="8">tivity</tspan></text>
      <circle cx="504" cy="331" r="16" fill="var(--coral)"/><text class="node-text" x="504" y="329">Future<tspan x="504" dy="8">Skills</tspan></text>
      <circle cx="521" cy="290" r="16" fill="var(--red)"/><text class="node-text" x="521" y="288">Gover<tspan x="521" dy="8">nment</tspan></text>
    </g>
    <text class="core-text core-text--plan" text-anchor="middle" transform="translate(572 318) rotate(45)">Skills<tspan x="0" dy="12">Planning</tspan></text>
    <text class="core-text core-text--renew" text-anchor="middle" transform="translate(551 340) rotate(45)">Skills<tspan x="0" dy="12">Renewal</tspan></text>

    <text class="label" x="317" y="183" text-anchor="end"><tspan class="label-b">Provision Planning</tspan><tspan x="317" dy="18">Regional Skills Plan</tspan></text>
    <text class="label" x="280" y="329" text-anchor="end"><tspan class="label-b">Skills Data</tspan><tspan x="280" dy="18">and </tspan><tspan class="label-b">Insights</tspan></text>
    <text class="label" x="317" y="476" text-anchor="end"><tspan class="label-b">Engagement</tspan> and<tspan x="317" dy="18" class="label-b">Collaboration</tspan> Front door</text>
    <text class="label" x="807" y="183"><tspan class="label-b">Skills Feedback</tspan><tspan x="807" dy="18">Employers and Students</tspan></text>
    <text class="label" x="840" y="329"><tspan class="label-b">Quality workforce</tspan><tspan x="840" dy="18">course design recognition</tspan></text>
    <text class="label label-b" x="807" y="486">Skills innovation</text>
  </svg>
  <div class="footer-brand"><span class="brand-dot"></span>KTR</div>
  <p class="copyright">Copyright © 2023  KTR</p>
  <div class="page-no">3</div>
</section>

<section class="slide slide--contact">
  <div class="pattern" role="img" aria-label="Woven red, berry and coral ribbon pattern"></div>
  <svg class="lens" viewBox="0 0 1124 632"><path d="M118,0 L470,0 Q690,140 780,316 Q690,490 470,632 L110,632 Q30,480 40,316 Q40,130 118,0 Z" fill="#000"/></svg>
  <div class="brand"><span class="brand-dot"></span><span class="brand-name">KTR</span></div>
  <h2 class="contact-heading">Contact Us</h2>
  <ul class="contact-list">
    <li><svg viewBox="0 0 24 24"><path d="M6 3 l4 4 -2 3 q2 4 6 6 l3 -2 4 4 -3 3 q-9 -1 -15 -12 z" fill="none" stroke="var(--red)" stroke-width="2"/></svg>Insert Phone Number</li>
    <li><svg viewBox="0 0 24 24"><circle cx="12" cy="12" r="4" fill="none" stroke="var(--berry)" stroke-width="2"/><path d="M16 8 v6 q0 3 3 2 q2 -2 2 -4 a9 9 0 1 0 -4 7" fill="none" stroke="var(--berry)" stroke-width="2"/></svg>Insert E-Mail Address</li>
    <li><svg viewBox="0 0 24 24"><circle cx="12" cy="12" r="9" fill="none" stroke="var(--orange)" stroke-width="2"/><path d="M3 12 h18 M12 3 q-5 9 0 18 M12 3 q5 9 0 18" fill="none" stroke="var(--orange)" stroke-width="2"/></svg>Insert URL Address</li>
  </ul>
</section>

</body>
</html>
```